VitaQuorb Web Design. Health and Wellness Industry

We are in process of creating next big Cloud based Health Care Management system. We have created 1st draft of Landing Page design. It is missing curb appeal, jazzy feel and engaging modern look.

Need a talented designer to recreate UI/ UX and take it to the next level.
If you are a creative designer, gifted with vision and imagination, I strongly encourage you to participate.

I want the designers to stay focus on the Landing page
Once we select the winner we will provide other subsequent pages
Follow up pages will be similar simple design

Target Market(s)

Individual Users and small business
Age Group 35-75
Individuals involved in "Health and Fitness" activity tracking, managing etc.

Industry/Entity Type

Health And Wellness

Number of Pages Required

5+ page

Colors
f68e4e
34a6d7

Requirements
Must have
• Super Engaging UI/ UX
• Smart and Contemporary look
• Easy to Navigate
• Folder Style menu bar
• Slideshow
• Social Medial Friendly
• Online Shopping
Nice to have
• Start from the enclosed draft Landing Page Idea.
• Feel Free to include additional frame, information section, Icon etc.

```html
<!DOCTYPE html>
<html lang="en">
<head>
<meta charset="utf-8">
<title>VitaQuorb – Organize Your Health Information</title>
<link href="https://fonts.googleapis.com/css2?family=Open+Sans:wght@300;400;600;700&family=Raleway:wght@300;400;600&display=swap" rel="stylesheet">
<style>
:root{
  --orange:#f68e4e;
  --blue:#34a6d7;
  --blue-dark:#2b93c2;
  --ink:#333;
  --muted:#777;
  --line:#e3e3e3;
  --soft:#f4f4f4;
  --footer:#ececec;
  --footer-bottom:#2f3438;
  --white:#fff;
}
*{box-sizing:border-box;margin:0;padding:0}
html,body{width:1200px;height:2172px;overflow:hidden}
body{font-family:"Open Sans",Arial,sans-serif;color:var(--ink);background:var(--white);font-size:14px}
a{color:inherit;text-decoration:none}

.topbar{height:112px;display:flex;align-items:center;justify-content:space-between;padding:0 28px}
.brand{display:flex;align-items:center;gap:12px;font-size:38px;font-weight:600;color:var(--orange)}
.brand-dot{width:28px;height:28px;border-radius:50%;background:var(--orange)}
.brand small{display:block;font-size:11px;color:var(--muted);font-weight:400;margin-top:-4px}
.top-actions{display:flex;align-items:center;gap:22px;font-size:13px;color:var(--muted)}
.btn-emergency{background:var(--orange);color:var(--white);padding:10px 22px;border-radius:3px;font-weight:600}
.lang{width:26px;height:16px;background:var(--blue);border-radius:2px}

.mainnav{height:40px;background:var(--blue);display:flex;align-items:center;padding:0 28px}
.mainnav a{color:var(--white);font-size:14px;font-weight:600;padding:0 34px 0 0;display:flex;align-items:center;gap:8px;white-space:nowrap}
.mainnav a.active{background:var(--blue-dark);padding:0 24px;height:40px;margin-right:10px}
.mainnav .search{margin-left:auto;width:230px;height:26px;background:var(--white);border-radius:2px;font-size:12px;color:#aaa;padding:5px 10px}

.hero{position:relative;height:440px;background:linear-gradient(110deg,#3c5466 0%,#6d8796 45%,#9fb1bb 100%)}
.hero-copy{position:absolute;left:28px;top:90px;color:var(--white)}
.hero h1{font-family:"Raleway",sans-serif;font-weight:300;font-size:66px;line-height:1.1;letter-spacing:1px}
.hero .explore{display:block;margin-top:16px;font-size:16px}
.dots{display:flex;gap:8px;justify-content:center}
.dots i{width:9px;height:9px;border-radius:50%;background:#ccc;display:block}
.dots i.on{background:var(--white)}
.hero .dots{position:absolute;bottom:14px;width:100%}

.features{height:400px;display:grid;grid-template-columns:repeat(4,1fr);padding:70px 60px 0}
.feature{text-align:center}
.feature svg{height:58px;width:58px}
.feature h2{font-size:24px;font-weight:400;margin:20px 0 14px;letter-spacing:1px}
.feature p{font-size:12px;line-height:1.7;color:var(--muted);padding:0 36px}

.stories{height:320px;position:relative;background:linear-gradient(180deg,#5b6266,#8e9498 60%,#b9bdc0)}
.stories h3{text-align:center;color:var(--white);font-size:18px;font-weight:600;padding-top:20px}
.quotes{display:flex;gap:40px;justify-content:center;margin-top:18px}
.quote{width:400px}
.quote p{background:var(--white);padding:14px 18px;font-size:12px;line-height:1.7;color:var(--muted);border:1px solid var(--line)}
.person{display:flex;align-items:center;gap:16px;margin-top:16px;color:var(--white)}
.avatar{width:58px;height:58px;border-radius:50%;background:#c9b8a8;border:3px solid var(--white)}
.person strong{display:block;font-size:15px}
.person span{font-size:12px}
.stories .dots{position:absolute;bottom:14px;width:100%}

.products{padding:40px 0 0;height:588px}
.products h3{text-align:center;font-size:24px;font-weight:400;letter-spacing:1px;margin-bottom:36px}
.grid{display:grid;grid-template-columns:repeat(4,220px);gap:60px;justify-content:center}
.card-img{height:240px;border-radius:2px;background:radial-gradient(circle at 50% 50%,#ffffff 0%,#e9edf0 70%,#dfe4e8 100%)}
.card-meta{display:flex;justify-content:space-between;align-items:center;height:36px;margin:12px 0 12px;font-size:12px}
.card-meta strong{font-weight:600;max-width:120px;line-height:1.4}
.card-meta span{font-size:17px}
.btn-cart{display:block;width:120px;margin:0 auto;border:1px solid var(--orange);color:var(--orange);text-align:center;font-size:12px;font-weight:600;padding:8px 0}
.products .dots{margin-top:40px}
.products .dots i{background:#999}
.products .dots i.on{background:#444}

.footer{background:var(--footer);height:192px;display:grid;grid-template-columns:repeat(4,1fr);padding:26px 28px 0}
.footer h4{font-size:14px;font-weight:700;margin-bottom:10px}
.footer li{list-style:none;font-size:12px;color:var(--muted);line-height:1.9}
.bottom{height:52px;background:var(--footer-bottom);display:flex;justify-content:space-between;align-items:center;padding:0 28px;color:#aaa;font-size:12px}
.social{display:flex;gap:12px}
.social i{width:20px;height:20px;border-radius:50%;background:#5c6368;display:block}
</style>
</head>
<body>
<header class="topbar">
  <a class="brand" href="#"><span class="brand-dot"></span><span>VitaQuorb<small>health management made simple</small></span></a>
  <div class="top-actions">
    <a class="btn-emergency" href="#">Emergency Login</a>
    <a href="#">Login</a><a href="#">Create an account</a><span class="lang"></span>
  </div>
</header>

<nav class="mainnav">
  <a class="active" href="#">Home</a>
  <a href="#">Discover CareLocker</a>
  <a href="#">Shop</a>
  <a href="#">Caregiver</a>
  <a href="#">Community</a>
  <div class="search">Search</div>
</nav>

<section class="hero" role="img" aria-label="Photo of a stethoscope lying on a laptop keyboard">
  <div class="hero-copy">
    <h1>ORGANIZE YOUR<br>HEALTH<br>INFORMATION</h1>
    <a class="explore" href="#">Explore VitaQuorb</a>
  </div>
  <div class="dots"><i class="on"></i><i></i><i></i></div>
</section>

<section class="features">
  <article class="feature">
    <svg viewBox="0 0 60 60"><path d="M4 30C14 14 46 14 56 30C46 46 14 46 4 30Z" fill="var(--orange)"/><circle cx="30" cy="30" r="11" fill="#fff"/><circle cx="30" cy="30" r="6" fill="var(--orange)"/></svg>
    <h2>OVERVIEW</h2>
    <p>Lorem Ipsum is simply dummy text of the printing and typesetting industry. Lorem Ipsum has been...</p>
  </article>
  <article class="feature">
    <svg viewBox="0 0 60 60" fill="#888"><circle cx="22" cy="34" r="14"/><circle cx="22" cy="34" r="5" fill="#fff"/><circle cx="44" cy="16" r="10"/><circle cx="44" cy="16" r="4" fill="#fff"/></svg>
    <h2>HOW IT WORKS</h2>
    <p>Lorem Ipsum is simply dummy text of the printing and typesetting industry. Lorem Ipsum has been...</p>
  </article>
  <article class="feature">
    <svg viewBox="0 0 60 60" fill="#888"><circle cx="30" cy="18" r="11"/><path d="M10 56C10 38 50 38 50 56Z"/></svg>
    <h2>STORIES</h2>
    <p>Lorem Ipsum is simply dummy text of the printing and typesetting industry. Lorem Ipsum has been...</p>
  </article>
  <article class="feature">
    <svg viewBox="0 0 60 60" fill="#888"><path d="M52 8C38 8 26 18 20 32L28 40C42 34 52 22 52 8Z"/><path d="M20 32L10 30L18 22L26 22Z"/><path d="M28 40L30 50L38 42L38 34Z"/><path d="M16 44L8 52L12 40Z"/></svg>
    <h2>GET STARTED</h2>
    <p>Lorem Ipsum is simply dummy text of the printing and typesetting industry. Lorem Ipsum has been...</p>
  </article>
</section>

<section class="stories" role="img" aria-label="Background photo of a doctor with a tablet">
  <h3>Find out ways people are using VitaQuorb CareLocker</h3>
  <div class="quotes">
    <div class="quote">
      <p>Lorem Ipsum is simply dummy text of the printing and typesetting industry. Lorem Ipsum has been the industry's standard dummy text ever since the 1500s, when an unknown printer took a galley of type and scrambled it to make a type specimen book.</p>
      <div class="person"><span class="avatar" role="img" aria-label="Portrait of John Smith"></span><div><strong>John Smith</strong><span>Developer</span></div></div>
    </div>
    <div class="quote">
      <p>Lorem Ipsum is simply dummy text of the printing and typesetting industry. Lorem Ipsum has been the industry's standard dummy text ever since the 1500s, when an unknown printer took a galley of type and scrambled it to make a type specimen book.</p>
      <div class="person"><span class="avatar" role="img" aria-label="Portrait of John Deo"></span><div><strong>John Deo</strong><span>Designer</span></div></div>
    </div>
  </div>
  <div class="dots"><i></i><i class="on"></i><i></i></div>
</section>

<section class="products">
  <h3>FEATURE PROJECTS</h3>
  <div class="grid">
    <article><div class="card-img" role="img" aria-label="Product photo of a glucose monitoring device"></div><div class="card-meta"><strong>Glucose Monitoring System</strong><span>$26.95</span></div><a class="btn-cart" href="#">ADD TO CART</a></article>
    <article><div class="card-img" role="img" aria-label="Product photo of a blood pressure cuff"></div><div class="card-meta"><strong>Blood Pressure Monitor</strong><span>$26.95</span></div><a class="btn-cart" href="#">ADD TO CART</a></article>
    <article><div class="card-img" role="img" aria-label="Product photo of a fitness tracker watch"></div><div class="card-meta"><strong>Health Sign</strong><span>$25.95</span></div><a class="btn-cart" href="#">ADD TO CART</a></article>
    <article><div class="card-img" role="img" aria-label="Product photo of a white sensor device"></div><div class="card-meta"><strong>Health Sign</strong><span>$26.95</span></div><a class="btn-cart" href="#">ADD TO CART</a></article>
  </div>
  <div class="dots"><i class="on"></i><i></i><i></i></div>
</section>

<footer>
  <div class="footer">
    <div><h4>COMPANY</h4><ul><li>About Us</li><li>The Buzz</li><li>Careers</li><li>Investors</li><li>Partner Options</li></ul></div>
    <div><h4>PRODUCTS</h4><ul><li>Blood Pressure Monitor</li><li>Glucose Monitor</li><li>Fitness Devices</li><li>Accessories</li><li>Store</li></ul></div>
    <div><h4>DOWNLOADS</h4><ul><li>Mobile Apps</li><li>Device Driver</li><li>API</li><li>Health Kit</li><li>Entertainment</li></ul></div>
    <div><h4>CONTACT</h4><ul><li>Support</li><li>Shipping Returns</li><li>Contact Us</li><li>Customers</li><li>Feedback</li></ul></div>
  </div>
  <div class="bottom"><span>© 2016 VitaQuorb. All rights reserved.</span><div class="social"><i></i><i></i><i></i><i></i><i></i></div></div>
</footer>
</body>
</html>
```